Need to have a client log in screen for work orders and estimate requests.
Nice informational landing page.

Stonefield is a full service general contractor servicing apartment complexes;
maintenance of grounds and apartments - remodeling and construction.

Design Specifics: We are pretty open here. Some good examples are
www.oakhavenworks.com , pellarestates.com and www.norvo7building.com

For the site we need:
Homepage - to explain services
Roofing page
Apartment Page
Client Portal - where clients can set up accounts to set up work/estimate request that will be routed to our email

--Will need coding, plan to host site on Wordpress

Target Market(s)

Multi family, Residential and commercial clients

Industry/Entity Type

Construction

Coding

Coded - Design and coding required

Number of Pages Required

3 page

Font styles to use
Serif

Requirements
Must have
• Client portal
Nice to have
• Not sure. please advise

```html
<!DOCTYPE html>
<html lang="en">
<head>
<meta charset="utf-8">
<title>Stonefield Construction</title>
<link rel="stylesheet" href="https://fonts.googleapis.com/css2?family=Open+Sans:wght@300;400;600;700&display=swap">
<style>
:root{
  --red:#b5120f;
  --red-line:#c0161b;
  --ink:#222;
  --body:#333;
  --muted:#555;
  --blue:#3a73c9;
  --link-blue:#3d7bd4;
  --panel:#f6f6f6;
  --white:#fff;
  --dark-card:#16191d;
}
*{margin:0;padding:0;box-sizing:border-box}
html,body{width:1200px;height:2857px;overflow:hidden;background:var(--white)}
body{position:relative;font-family:"Open Sans",Arial,sans-serif;color:var(--body)}
.abs{position:absolute}
p{font-size:11.5px;line-height:19px}
.justify{text-align:justify}

/* header */
.site-header{left:0;top:0;width:1200px;height:78px;border-bottom:2px solid var(--red-line);background:var(--white)}
.brand{display:flex;align-items:center;gap:8px}
.brand-mark{width:22px;height:22px;background:var(--red)}
.brand-name{font-weight:700;font-size:22px;letter-spacing:1px;color:var(--ink)}
.main-nav{left:372px;top:26px;display:flex;gap:0;font-size:13px}
.main-nav a{color:var(--ink);text-decoration:none;margin-right:34px}
.main-nav a.active{color:var(--red);border-bottom:2px solid var(--red);padding-bottom:4px}
.auth-box{left:785px;top:24px;width:128px;height:28px;border:1px solid #444;font-size:10.5px;display:flex;align-items:center;justify-content:center;gap:10px;color:var(--ink)}
.social{display:flex;gap:11px}
.social span{width:20px;height:20px;border:1px solid #777;border-radius:50%;display:block}

/* hero */
.hero-photo{left:0;top:80px;width:1200px;height:408px;background:linear-gradient(90deg,#fff 0%,#fff 20%,#d7dde3 34%,#7d8fa1 55%,#4a5866 75%,#a9b7c3 100%)}
.hero-arrow{width:34px;height:32px;border:1px solid #222;background:var(--white);display:flex;align-items:center;justify-content:center}

/* about band */
.sky-band{left:0;top:665px;width:1200px;height:448px;background:linear-gradient(180deg,#a9b8cc 0%,#d9b49a 55%,#e8a36c 80%,#9a8a80 100%)}
.intro-panel{left:150px;top:540px;width:900px;height:508px;background:var(--panel)}
.intro-col h2{font-weight:400;font-size:23px;color:var(--ink);display:inline-block;border-bottom:2px solid var(--ink);padding-bottom:1px;margin-bottom:14px}
.intro-col p{width:225px}
.btn-outline{display:inline-block;margin-top:20px;border:1px solid #333;font-size:10.5px;padding:3px 14px;color:var(--ink);background:var(--white)}
.roofer-photo{left:452px;top:597px;width:304px;height:393px;background:linear-gradient(180deg,#cfd3d6 0%,#b9bfbf 35%,#7b6a5d 70%,#5d4b40 100%)}

/* apartment */
.apartment-photo{left:0;top:1113px;width:1200px;height:597px;background:linear-gradient(90deg,#7a6f63 0%,#d9c6a3 25%,#8e9aa6 45%,#a9cbe2 70%,#cfe3ea 100%)}
.apartment-card{left:552px;top:1200px;width:458px;height:432px;background:var(--white)}
.apartment-card h2{position:absolute;left:48px;top:36px;font-weight:400;font-size:34px;color:var(--ink)}
.card-arrows{position:absolute;left:394px;top:52px;display:flex;gap:8px}
.card-arrows span{width:20px;height:20px;border:1px solid #666;border-radius:50%;display:flex;align-items:center;justify-content:center}
.step{position:absolute;left:48px;display:flex;gap:26px}
.step-num{width:75px;height:58px;background:var(--blue);color:var(--white);font-size:28px;font-weight:300;display:flex;align-items:center;justify-content:center}
.step h3{font-weight:400;font-size:13.5px;color:var(--link-blue);margin-top:2px;margin-bottom:4px}
.step p{font-size:10.5px;line-height:17px;width:270px;color:var(--ink)}

/* services */
.section-title{left:0;width:1200px;text-align:center;font-weight:400;font-size:36px;color:var(--ink)}
.service-card{top:1825px;width:282px;height:352px;background:linear-gradient(180deg,#3a3f45 0%,#1d2126 45%,#0f1114 100%);color:var(--white);text-align:center}
.service-icon{margin:32px auto 0;width:86px;height:86px;border-radius:50%;background:var(--blue);display:flex;align-items:center;justify-content:center}
.service-card h3{font-weight:600;font-size:16px;margin-top:20px}
.service-card p{font-size:10.5px;line-height:18px;margin:22px auto 0;width:240px;color:#e6e6e6}
.service-card a{display:inline-block;margin-top:22px;font-size:10.5px;color:var(--white);text-decoration:underline}

/* get started */
.get-started{left:150px;top:2222px;width:640px;height:475px;background:var(--red)}
.get-started h2{position:absolute;left:32px;top:42px;color:var(--white);font-weight:400;font-size:34px}
.field{position:absolute;width:266px;height:35px;border:1px solid #f0b5b3;color:var(--white);font-size:12.5px;padding:8px 12px;display:flex;justify-content:space-between;align-items:center}
.submit{position:absolute;left:32px;top:366px;width:576px;height:54px;background:var(--white);color:var(--red);font-size:14px;display:flex;align-items:center;justify-content:center}

.info-col{left:825px;width:236px}
.info-col h2{font-weight:400;font-size:40px;color:var(--ink);line-height:44px}
.info-col p{font-size:11.5px;line-height:21.5px;color:var(--ink)}

/* footer */
.footer-nav{left:0;top:2787px;width:1200px;text-align:center;font-size:10px;color:var(--ink)}
.footer-nav span{margin:0 10px}
.copyright{left:0;top:2812px;width:1200px;text-align:center;font-size:10px;color:var(--muted)}
</style>
</head>
<body>

<header class="site-header abs">
  <div class="brand abs" style="left:150px;top:26px">
    <span class="brand-mark"></span><span class="brand-name">STONEFIELD</span>
  </div>
  <nav class="main-nav abs">
    <a class="active" href="#">Home</a><a href="#">Services</a><a href="#">Roofing</a><a href="#">Apartment</a><a href="#">Contact Us</a>
  </nav>
  <div class="auth-box abs"><span>Login</span><span>|</span><span>Register</span></div>
  <div class="social abs" style="left:966px;top:27px"><span></span><span></span><span></span></div>
</header>

<section>
  <div class="hero-photo abs" role="img" aria-label="Photo of a construction team reviewing building models in a bright glass office"></div>
  <div class="hero-arrow abs" style="left:115px;top:258px"><svg width="16" height="16" viewBox="0 0 16 16"><circle cx="8" cy="8" r="7" fill="none" stroke="#222" stroke-width="1.5"/><path d="M9.5 4.5 6 8l3.5 3.5" fill="none" stroke="#222" stroke-width="1.5"/></svg></div>
  <div class="hero-arrow abs" style="left:1050px;top:258px"><svg width="16" height="16" viewBox="0 0 16 16"><circle cx="8" cy="8" r="7" fill="none" stroke="#222" stroke-width="1.5"/><path d="M6.5 4.5 10 8l-3.5 3.5" fill="none" stroke="#222" stroke-width="1.5"/></svg></div>
</section>

<section>
  <div class="sky-band abs" role="img" aria-label="Steel scaffolding silhouettes against a sunset sky"></div>
  <div class="intro-panel abs"></div>
  <div class="intro-col abs" style="left:188px;top:652px">
    <h2>About Us</h2>
    <p class="justify">There are many variations of passages of Lorem Ipsum available, but the majority have suffered alteration in some form, by injected humour, or randomised words which don't look even slightly believable. If you are going to use a passage of Lorem Ipsum, you need to be sure there isn't anything embarrassing hidden in the middle of text.</p>
    <span class="btn-outline">Read More</span>
  </div>
  <div class="roofer-photo abs" role="img" aria-label="Photo of a roofer in a safety vest working on a shingle roof"></div>
  <div class="intro-col abs" style="left:790px;top:652px">
    <h2>Roofing</h2>
    <p class="justify">There are many variations of passages of Lorem Ipsum available, but the majority have suffered alteration in some form, by injected humour, or randomised words which don't look even slightly believable. If you are going to use a passage of Lorem Ipsum, you need to be sure there isn't anything embarrassing hidden in the middle of text.</p>
    <span class="btn-outline">Read More</span>
  </div>
</section>

<section>
  <div class="apartment-photo abs" role="img" aria-label="Photo of a modern apartment building with balconies under a clear sky"></div>
  <div class="apartment-card abs">
    <h2>Apartment</h2>
    <div class="card-arrows">
      <span><svg width="10" height="10" viewBox="0 0 10 10"><path d="M8 5H2M4.5 2.5 2 5l2.5 2.5" fill="none" stroke="#444" stroke-width="1.3"/></svg></span>
      <span><svg width="10" height="10" viewBox="0 0 10 10"><path d="M2 5h6M5.5 2.5 8 5 5.5 7.5" fill="none" stroke="#444" stroke-width="1.3"/></svg></span>
    </div>
    <div class="step" style="top:110px"><div class="step-num">1</div><div><h3>Many variations of passages of Ipsum available</h3><p>There are many variations of passages of Lorem Ipsum available, but the majority.</p></div></div>
    <div class="step" style="top:208px"><div class="step-num">2</div><div><h3>Many variations of passages of Ipsum available</h3><p>There are many variations of passages of Lorem Ipsum available, but the majority.</p></div></div>
    <div class="step" style="top:308px"><div class="step-num">3</div><div><h3>Many variations of passages of Ipsum available</h3><p>There are many variations of passages of Lorem Ipsum available, but the majority.</p></div></div>
  </div>
</section>

<section>
  <h2 class="section-title abs" style="top:1748px">Services</h2>
  <div class="service-card abs" style="left:150px" role="img" aria-label="Service card over a dim photo of a construction site">
    <div class="service-icon"><svg width="48" height="40" viewBox="0 0 48 40" fill="none" stroke="#fff" stroke-width="2.5"><path d="M4 20 24 4l20 16"/><path d="M10 16v20h28V16"/><path d="M20 36V24h8v12"/></svg></div>
    <h3>Sheets Containing</h3>
    <p class="justify">There are many variations of passages of Lorem Ipsum available, but the majority have suffered alteration in some form, by injected humour, or randomised words which don't look even slightly believable.</p>
    <a href="#">Read More</a>
  </div>
  <div class="service-card abs" style="left:459px" role="img" aria-label="Service card over a dim photo of a construction site">
    <div class="service-icon"><svg width="44" height="44" viewBox="0 0 44 44"><circle cx="22" cy="22" r="13" fill="none" stroke="#fff" stroke-width="6" stroke-dasharray="6 4.2"/><circle cx="22" cy="22" r="10" fill="none" stroke="#fff" stroke-width="3"/><circle cx="22" cy="22" r="4" fill="#fff"/></svg></div>
    <h3>Sheets Containing</h3>
    <p class="justify">There are many variations of passages of Lorem Ipsum available, but the majority have suffered alteration in some form, by injected humour, or randomised words which don't look even slightly believable.</p>
    <a href="#">Read More</a>
  </div>
  <div class="service-card abs" style="left:767px" role="img" aria-label="Service card over a dim photo of a construction site">
    <div class="service-icon"><svg width="40" height="44" viewBox="0 0 40 44" fill="none" stroke="#fff" stroke-width="2.2"><rect x="7" y="4" width="26" height="36"/><path d="M13 11h4M23 11h4M13 18h4M23 18h4M13 25h4M23 25h4M17 40v-7h6v7"/></svg></div>
    <h3>Sheets Containing</h3>
    <p class="justify">There are many variations of passages of Lorem Ipsum available, but the majority have suffered alteration in some form, by injected humour, or randomised words which don't look even slightly believable.</p>
    <a href="#">Read More</a>
  </div>
</section>

<section>
  <form class="get-started abs">
    <h2>Get Started</h2>
    <div class="field" style="left:32px;top:116px">FIRST NAME</div>
    <div class="field" style="left:342px;top:116px">LAST NAME</div>
    <div class="field" style="left:32px;top:175px">EMAIL ADDRESS</div>
    <div class="field" style="left:342px;top:175px">PHONE NUMBER</div>
    <div class="field" style="left:32px;top:234px">COMPANY</div>
    <div class="field" style="left:342px;top:234px">TITLE</div>
    <div class="field" style="left:32px;top:293px">COUNTRY<svg width="12" height="8" viewBox="0 0 12 8"><path d="M0 0h12L6 8z" fill="#fff"/></svg></div>
    <div class="field" style="left:342px;top:293px">CITY<svg width="12" height="8" viewBox="0 0 12 8"><path d="M0 0h12L6 8z" fill="#fff"/></svg></div>
    <div class="submit">GET STARTED NOW !</div>
  </form>

  <div class="info-col abs" style="top:2246px">
    <h2>COMPANY</h2>
    <p class="justify">Contrary to popular belief, Lorem Ipsum is not simply random text. It has roots in a piece of classical Latin literature from 45 BC, making it over 2000 years old. Edwin Harlow, a Latin professor at Ashbury College in Vermont, looked up one of the more obscure Latin words, consectetur, from a Lorem Ipsum passage, and going through the cites of the word in classical literature, discovered the undoubtable source.</p>
  </div>
  <div class="info-col abs" style="top:2535px">
    <h2>CONTACT</h2>
    <p style="font-size:10.5px;line-height:19px;margin-top:4px">The standard chunk of Lorem Ipsum used since the 1500s is reproduced below for those interested.</p>
    <p style="font-size:14px;margin-top:4px">0147 2280 365</p>
    <p style="font-size:10.5px">info@stonefieldbuild.co.uk</p>
    <div class="social" style="margin-top:8px;gap:10px"><span></span><span></span><span></span></div>
  </div>
</section>

<footer>
  <div class="brand abs" style="left:522px;top:2735px">
    <span class="brand-mark"></span><span class="brand-name">STONEFIELD</span>
  </div>
  <div class="footer-nav abs"><span>Home</span>|<span>Services</span>|<span>Roofing</span>|<span>Apartment</span>|<span>Contact Us</span></div>
  <div class="copyright abs">© 2016 Stonefield Construction. All rights reserved.</div>
</footer>

</body>
</html>
```